strength and conditioning business focused on helping people move more efficiently

I need a business card designed for a Philadelphia based company called Brk Stn Motion (pronounced Brick Stone). We offer fitness professional services with the idea of helping people feel better and move optimally. We do this by designing and walking through individualized programs as well as minor soft tissue work. Our perfect client would be athletes but we will be marketing to parents who have children that are active They remember their former athletic days and want to get as close as possible back to that feeling. Attached will be the official logo and logo formats. I would love for the design to communicate trustworthy and creative. I would also love for the design to be square with rounded edges.

Target Market(s)

Parents of athletic children
former athletes
athletes

Industry/Entity Type

Fitness

Contact Information for Business Card

Business: Brk Stn Athletics
Name: Coach Gareth Milford
Position: Strength and Conditioning Coach / Certified Personal Trainer
Contact: coach.mil@brkstn.example
Text: (555)204-7719

Font styles to use
Serif
Sans Serif

Colors
fbee38
fbee3e
0255a3
3176b5
ffffff

Requirements
Must have
• use of logo
Nice to have
• Square design
rounded edges

```html
<!DOCTYPE html>
<html lang="en">
<head>
<meta charset="utf-8">
<title>Brk Stn Motion — Business Card</title>
<link rel="stylesheet" href="https://fonts.googleapis.com/css2?family=Arimo:wght@400;700&display=swap">
<style>
  :root {
    --navy: #0b3082;
    --navy-deep: #082a72;
    --yellow: #f6c915;
    --white: #ffffff;
    --ink: #2b2b2b;
    --stage: #ececec;
  }
  * { box-sizing: border-box; margin: 0; padding: 0; }
  html, body {
    width: 1200px;
    height: 859px;
    overflow: hidden;
    background: var(--stage);
    font-family: "Arimo", Arial, sans-serif;
  }
  .canvas { position: relative; width: 1200px; height: 859px; }

  .card {
    position: absolute;
    top: 208px;
    width: 446px;
    height: 445px;
    border-radius: 24px;
    overflow: hidden;
    box-shadow: 0 4px 14px rgba(0,0,0,0.18);
  }
  .card--front { left: 142px; background: var(--white); }
  .card--back  {
    left: 626px;
    background: linear-gradient(135deg, var(--navy) 0%, var(--navy-deep) 100%);
  }

  .brand {
    position: absolute;
    display: flex;
    align-items: center;
    gap: 12px;
  }
  .brand__dot {
    width: 42px; height: 42px;
    border-radius: 50%;
    background: var(--yellow);
    flex: none;
  }
  .brand__name {
    font-weight: 700;
    font-size: 44px;
    letter-spacing: 0.5px;
    white-space: nowrap;
    line-height: 1;
  }
  .card--front .brand { left: 24px; top: 112px; }
  .card--front .brand__name { color: var(--navy); }
  .card--back .brand { left: 38px; top: 190px; }
  .card--back .brand__name { color: var(--white); }

  .person {
    position: absolute;
    left: 0;
    top: 246px;
    padding-left: 24px;
  }
  .person__bar {
    position: absolute;
    left: 0; top: 0;
    width: 9px; height: 58px;
    background: var(--navy);
  }
  .person__name {
    font-weight: 700;
    font-size: 21px;
    color: var(--navy);
    line-height: 1.2;
  }
  .person__name .honorific { color: var(--yellow); }
  .person__role {
    margin-top: 3px;
    font-size: 15px;
    line-height: 19px;
    color: var(--ink);
  }

  .contacts {
    position: absolute;
    left: 22px;
    top: 354px;
    list-style: none;
  }
  .contacts li {
    display: flex;
    align-items: center;
    gap: 7px;
    font-size: 15.5px;
    line-height: 21.5px;
    color: var(--ink);
  }
  .contacts svg { width: 11px; height: 11px; fill: var(--navy); flex: none; }
</style>
</head>
<body>
<main class="canvas">

  <section class="card card--front" aria-label="Card front">
    <div class="brand">
      <span class="brand__dot"></span>
      <span class="brand__name">Brk Stn Motion</span>
    </div>

    <div class="person">
      <span class="person__bar"></span>
      <p class="person__name"><span class="honorific">Coach</span> <span class="honorific">Gareth</span> Milford</p>
      <p class="person__role">Strength and Conditioning Coach /<br>Certified Personal Trainer</p>
    </div>

    <ul class="contacts">
      <li>
        <svg viewBox="0 0 12 12" aria-hidden="true"><path d="M2.5 0.8l2 2.1-1 1.3c.6 1.5 1.8 2.8 3.3 3.4l1.3-1 2.1 2-1.2 2.2C4.6 10.6 1.4 7.4.6 2z"/></svg>
        (555)204-7719
      </li>
      <li>
        <svg viewBox="0 0 12 12" aria-hidden="true"><path d="M0 2h12v1.2L6 7 0 3.2z M0 4.5l6 3.8 6-3.8V10H0z"/></svg>
        coach.mil@brkstn.example
      </li>
      <li>
        <svg viewBox="0 0 12 12" aria-hidden="true"><circle cx="6" cy="6" r="5.6"/><path d="M0.6 6h10.8M6 0.4c-3 3-3 8.2 0 11.2M6 0.4c3 3 3 8.2 0 11.2" stroke="#fff" stroke-width="0.9" fill="none"/></svg>
        www.brkstn.example
      </li>
    </ul>
  </section>

  <section class="card card--back" aria-label="Card back">
    <div class="brand">
      <span class="brand__dot"></span>
      <span class="brand__name">Brk Stn Motion</span>
    </div>
  </section>

</main>
</body>
</html>
```